Revamp Landing Page

Our current landing page is http://lanternpubkq.com/ and we're looking for our site to look like this http://www.amberroomvk.com/. Classy, Sleek, Simple elegant.

The site should be desktop and mobile optimized.
Pages should be built out and the same structure. Drink Menu, Gallery, Events, Table Reservations, Membership, Press, Contact Us.

Feel free to use the images on our website.

```html
<!DOCTYPE html>
<html lang="en">
<head>
<meta charset="utf-8">
<title>Lantern Pub – Mobile Landing</title>
<link rel="stylesheet" href="https://fonts.googleapis.com/css2?family=Open+Sans:wght@300;400;600;700&display=swap">
<style>
  :root {
    --gold: #c79c55;
    --gold-deep: #b8893f;
    --paper: #f8f1ee;
    --band: #f1e2dc;
    --ink: #1b1b1b;
    --muted: #9a7a4a;
    --shadow: #b58a45;
    --white: #ffffff;
  }
  * { margin: 0; padding: 0; box-sizing: border-box; }
  html, body { width: 1200px; height: 858px; overflow: hidden; }
  body {
    background: var(--gold);
    font-family: "Open Sans", sans-serif;
    position: relative;
  }
  .board-label {
    position: absolute; top: 70px; left: 0; width: 1200px;
    text-align: center; color: var(--white);
    font-size: 16px; font-weight: 400;
  }
  .card-shadow {
    position: absolute; left: 369px; top: 163px; width: 389px; height: 631px;
    background: var(--shadow); filter: blur(2px); opacity: .8;
  }
  .card {
    position: absolute; left: 395px; top: 151px; width: 391px; height: 632px;
    background: var(--paper);
  }
  .brand {
    position: absolute; top: 48px; left: 0; width: 100%;
    text-align: center; font-size: 30px; font-weight: 300;
    letter-spacing: 2px; color: var(--ink);
  }
  .frame {
    position: absolute; left: 20px; top: 130px; width: 350px; height: 332px;
    border: 1px solid var(--gold);
  }
  .frame-gap-top {
    position: absolute; left: 101px; top: -2px; width: 143px; height: 4px;
    background: var(--paper);
  }
  .frame-gap-bottom {
    position: absolute; left: 29px; bottom: -2px; width: 292px; height: 4px;
    background: var(--paper);
  }
  .menu-toggle {
    position: absolute; left: 0; top: 121px; width: 100%;
    display: flex; justify-content: center; align-items: center; gap: 12px;
    font-size: 13px; letter-spacing: 1.5px; color: var(--ink);
  }
  .hero {
    position: absolute; left: 37px; top: 152px; width: 318px; height: 284px;
    background: linear-gradient(160deg, #2a1d3a 0%, #6e1d22 30%, #8a5f55 55%, #4a3a34 80%, #2a201c 100%);
  }
  .hero-title {
    position: absolute; left: 21px; top: 119px; width: 190px;
    color: var(--gold); font-size: 11px; font-weight: 700; line-height: 14px;
  }
  .hero-text {
    position: absolute; left: 21px; top: 167px; width: 195px;
    color: var(--white); font-size: 10px; line-height: 12.6px;
  }
  .btn-reserve {
    position: absolute; left: 21px; top: 225px; width: 167px; height: 33px;
    background: var(--gold); color: var(--white);
    font-size: 10px; font-weight: 700; letter-spacing: 1.8px;
    display: flex; align-items: center; justify-content: center;
  }
  .social {
    position: absolute; left: 0; top: 453px; width: 100%;
    display: flex; justify-content: center; gap: 11px;
    font-size: 10px; letter-spacing: 1px; color: var(--muted);
  }
  .social-item { display: flex; align-items: center; gap: 6px; }
  .social-dot { width: 8px; height: 8px; border-radius: 50%; background: var(--muted); }
  .events-band {
    position: absolute; left: 0; top: 510px; width: 100%; height: 43px;
    background: var(--band);
    display: flex; align-items: center; justify-content: center; gap: 6px;
    font-size: 11.5px; color: var(--ink);
  }
  .events-band a { color: var(--ink); font-weight: 700; text-decoration: underline; }
  .contact {
    position: absolute; left: 0; top: 579px; width: 100%;
    text-align: center; font-size: 10px; letter-spacing: 1.2px;
    line-height: 13px; color: var(--ink);
  }
</style>
</head>
<body>
  <div class="board-label">Mobile Version</div>
  <div class="card-shadow"></div>
  <main class="card">
    <div class="brand">LANTERN PUB</div>
    <div class="frame">
      <div class="frame-gap-top"></div>
      <div class="frame-gap-bottom"></div>
    </div>
    <div class="menu-toggle">
      <span>MENU</span>
      <svg width="21" height="13" viewBox="0 0 21 13">
        <g stroke="#c79c55" stroke-width="1.4">
          <line x1="0" y1="1" x2="21" y2="1"/>
          <line x1="0" y1="6.5" x2="21" y2="6.5"/>
          <line x1="0" y1="12" x2="21" y2="12"/>
        </g>
      </svg>
    </div>
    <section class="hero" role="img" aria-label="Night photo of the pub entrance under a red neon sign">
      <h1 class="hero-title">LANTERN PUB: A HOME AWAY FROM HOME FOR THE LOCAL COMMUNITY.</h1>
      <p class="hero-text">At Lantern Pub, it is our goal to make sure that you enjoy every moment in your experience. Consider us your liaisons to happiness...</p>
      <div class="btn-reserve">TABLE RESERVATIONS</div>
    </section>
    <nav class="social">
      <span class="social-item"><i class="social-dot"></i>FRIENDBOOK</span>
      <span class="social-item"><i class="social-dot"></i>CHIRPER</span>
      <span class="social-item"><i class="social-dot"></i>SNAPGRAM</span>
    </nav>
    <div class="events-band">
      <span>Want to Book a Private Party?</span>
      <a href="#">Check Out Our Events Deck</a>
    </div>
    <address class="contact" style="font-style:normal">
      48 Harbor Ln Bayview, California 90211<br>
      Info@lanternpubkq.com
    </address>
  </main>
</body>
</html>
```